Conflict prevention NGO needs business cards ASAP

We are a small NGO based in New Caledonia working on conflict prevention, and will be attending a OGA-sponsored conference on small arms next month. Our work involves campaigning against the proliferation of small arms in this post-conflict South Pacific island, and we need business cards to match that purpose.
Our three basic guidelines are the following:
1. We would like the logo of our organisation (see attached) included on this card. We are open to a redesign of this logo to something more stylised or abstract.
2. The card would need to be double-sided: one side in French, the other in English. The text should ideally be minimalist, uncluttered, clear and concise. We prefer the card to visually communicate our mission. As such, we would like the card to present a central image or logo, which would give us the option of printing a texture onto that image/logo later.
3. I have attached images which might inspire the designer (bullets and the famous knotted gun statue). However, these are NOT prescriptive; they are simply thematic ideas, and designers should use their own creative license. We only ask that the overall business card communicate professionalism and a seriousness of purpose, rather than sentimentalism or idealism.
Thanks to everyone who is willing to offer up a design idea! I am grateful for your time, and look forward to viewing your ideas. I apologise, but this has to be a rush job. Please get in touch if you need further guidance.
Please note that our new website will go live on Wednesday evening (Brisbane time), in case it can provide inspiration: http://www.portlumineux.org/
ENGLISH SIDE
[Name, Position] Kieran Vasko, Director
[Organisation] The Centre for a Bright Harbour
[Sub-Title] The first New Caledonian think tank
[Tel] +61407913222
[Email] centreportlumineux@postvale.net
[Website] http://www.portlumineux.org/
FRENCH SIDE
[Name, Position] Kieran Vasko, Directeur
[Organisation] Le Centre pour le Port Lumineux
[Sub-Title] Le premier pôle de réflexion calédonien
[Tel] +61407913222
*Note: We are flexible on the exact way you present the above information, and you may wish to use icons instead of "Tel." for example.

```html
<!DOCTYPE html>
<html lang="en">
<head>
<meta charset="utf-8">
<title>Business cards – The Centre for a Bright Harbour</title>
<link rel="stylesheet" href="https://fonts.googleapis.com/css2?family=Exo+2:wght@400;600;700&display=swap">
<style>
  :root {
    --page-bg: #d9d9d9;
    --card-white: #f7f7f7;
    --card-black: #050505;
    --ink: #111111;
    --ink-soft: #333333;
    --ink-light: #d6d6d6;
    --rule: #555555;
    --brand-blue: #1f7cc4;
    --band-text: #ffffff;
  }
  * { box-sizing: border-box; margin: 0; padding: 0; }
  html, body { width: 1200px; height: 864px; overflow: hidden; }
  body {
    background: var(--page-bg);
    font-family: "Exo 2", sans-serif;
    color: var(--ink);
    display: flex;
    flex-direction: column;
    align-items: center;
    justify-content: center;
    gap: 24px;
  }
  .card {
    width: 700px;
    height: 400px;
    position: relative;
    overflow: hidden;
    box-shadow: 0 6px 18px rgba(0,0,0,0.18);
  }

  /* English side */
  .card--front { background: var(--card-white); }
  .org-mark {
    position: absolute;
    left: 78px;
    top: 62px;
    width: 200px;
    height: 200px;
    border: 10px solid var(--brand-blue);
    background: var(--card-white);
  }
  .org-name {
    position: absolute;
    left: 50px;
    top: 282px;
    width: 256px;
    text-align: center;
    font-size: 17px;
    font-weight: 400;
    color: var(--ink-soft);
  }
  .divider {
    position: absolute;
    left: 345px;
    top: 62px;
    width: 1px;
    height: 280px;
    background: var(--rule);
  }
  .person {
    position: absolute;
    left: 390px;
    top: 120px;
  }
  .person-name {
    font-size: 28px;
    font-weight: 700;
    letter-spacing: 1px;
    text-transform: uppercase;
    line-height: 1;
  }
  .person-role {
    font-size: 14px;
    font-weight: 600;
    letter-spacing: 1px;
    text-transform: uppercase;
    margin-top: 4px;
  }
  .contacts {
    position: absolute;
    left: 390px;
    top: 222px;
    list-style: none;
  }
  .contacts li {
    display: flex;
    align-items: center;
    gap: 12px;
    font-size: 16px;
    line-height: 26px;
  }
  .contacts svg { width: 15px; height: 15px; flex: none; }

  /* French side */
  .card--back { background: var(--card-black); color: var(--band-text); }
  .photo-area {
    position: absolute;
    left: 0; top: 0;
    width: 700px;
    height: 322px;
    background:
      radial-gradient(ellipse 60% 70% at 45% 70%, rgba(196,160,80,0.55), transparent 70%),
      radial-gradient(ellipse 25% 50% at 88% 72%, rgba(200,40,40,0.7), transparent 75%),
      linear-gradient(180deg, #0c0c0c 0%, #1c1c1c 70%, #2a2a2a 100%);
  }
  .back-details {
    position: absolute;
    left: 36px;
    top: 30px;
  }
  .back-details .person-name { font-size: 24px; }
  .back-details .person-role { font-size: 13px; color: var(--ink-light); }
  .back-org {
    margin-top: 14px;
    font-size: 15px;
    font-weight: 400;
    color: var(--ink-light);
  }
  .back-phone {
    margin-top: 6px;
    display: flex;
    align-items: center;
    gap: 10px;
    font-size: 15px;
    color: var(--ink-light);
  }
  .back-phone svg { width: 14px; height: 14px; flex: none; }
  .tagline {
    position: absolute;
    left: 0; bottom: 0;
    width: 100%;
    height: 78px;
    display: flex;
    align-items: center;
    justify-content: center;
    font-size: 21px;
    font-weight: 600;
    letter-spacing: 1px;
    text-transform: uppercase;
  }
</style>
</head>
<body>

  <section class="card card--front" aria-label="English side">
    <div class="org-mark" aria-hidden="true"></div>
    <p class="org-name">The Centre for a Bright Harbour</p>
    <div class="divider"></div>
    <div class="person">
      <h1 class="person-name">Kieran Vasko</h1>
      <p class="person-role">Director</p>
    </div>
    <ul class="contacts">
      <li>
        <svg viewBox="0 0 16 16" aria-hidden="true"><path fill="#111" d="M3 5c0-2 2-3 5-3s5 1 5 3v1h-3V5H6v1H3z M4 8h8l2 6H2z"/></svg>
        +61407913222
      </li>
      <li>
        <svg viewBox="0 0 16 16" aria-hidden="true"><rect x="1.5" y="2.5" width="13" height="9" fill="none" stroke="#111" stroke-width="1.5"/><path d="M5 14h6" stroke="#111" stroke-width="1.5"/></svg>
        centreportlumineux@postvale.net
      </li>
      <li>
        <svg viewBox="0 0 16 16" aria-hidden="true"><rect x="1" y="3" width="14" height="10" fill="#111"/><path d="M1.5 3.5 8 9l6.5-5.5" fill="none" stroke="#f7f7f7" stroke-width="1.2"/></svg>
        www.portlumineux.org
      </li>
    </ul>
  </section>

  <section class="card card--back" lang="fr" aria-label="French side">
    <div class="photo-area" role="img" aria-label="Photograph of a row of cartridges of rising size, from small pistol rounds to rifle rounds and two red shotgun shells, on a dark background"></div>
    <div class="back-details">
      <h2 class="person-name">Kieran Vasko</h2>
      <p class="person-role">Directeur</p>
      <p class="back-org">Le Centre pour le Port Lumineux</p>
      <p class="back-phone">
        <svg viewBox="0 0 16 16" aria-hidden="true"><path fill="#d6d6d6" d="M3 5c0-2 2-3 5-3s5 1 5 3v1h-3V5H6v1H3z M4 8h8l2 6H2z"/></svg>
        +61407913222
      </p>
    </div>
    <p class="tagline">Le premier pôle de réflexion calédonien</p>
  </section>

</body>
</html>
```